Oven Cleaning Business owner needs business card design

Hi there,
Would like for a business card to be designed for myself, the owner of a professional oven cleaning business on the Sunshine Coast.
Would like it to look sleek, and modern-ish. Bit creative is encouraged too.
Include following:
Name/title: Corin ter Haghe, Owner
Phone number: 1300 482 916
Email: info@hearthshinecrew.com.au
Website: www.hearthshinecrew.com.au

```html
<!DOCTYPE html>
<html lang="en">
<head>
<meta charset="utf-8">
<title>Hearthshine Crew – Business Card</title>
<link rel="stylesheet" href="https://fonts.googleapis.com/css2?family=Poppins:ital,wght@0,300;0,400;0,800;1,300;1,400;1,800&display=swap">
<style>
  :root {
    --teal: #52c3cb;
    --ink: #0d0d0d;
    --paper: #ffffff;
    --backdrop: #ececec;
  }
  * { box-sizing: border-box; margin: 0; padding: 0; }
  html, body {
    width: 1200px;
    height: 1200px;
    overflow: hidden;
    background: var(--backdrop);
    font-family: "Poppins", sans-serif;
  }
  .card {
    position: absolute;
    left: 142px;
    width: 916px;
    height: 533px;
    overflow: hidden;
    box-shadow: 0 2px 6px rgba(0,0,0,0.18);
  }
  .card-back { top: 52px; background: var(--teal); color: var(--paper); }
  .card-front { top: 606px; background: var(--paper); }
  .card-art { position: absolute; inset: 0; width: 916px; height: 533px; }

  .back-brand {
    position: absolute;
    left: 70px;
    top: 235px;
    font-weight: 800;
    font-size: 34px;
    color: var(--paper);
    letter-spacing: 0.5px;
  }

  .holder {
    position: absolute;
    right: 62px;
    top: 210px;
    text-align: right;
  }
  .holder-name { font-weight: 800; font-style: italic; font-size: 32px; line-height: 1.15; color: var(--ink); }
  .holder-role { font-weight: 400; font-style: italic; font-size: 30px; line-height: 1.25; color: var(--ink); }

  .contacts {
    position: absolute;
    right: 38px;
    top: 342px;
    list-style: none;
  }
  .contact {
    display: flex;
    align-items: center;
    justify-content: flex-end;
    gap: 24px;
    height: 42px;
    font-weight: 300;
    font-size: 22px;
    color: var(--ink);
  }
  .contact svg { width: 16px; height: 16px; flex: none; }

  .front-brand {
    position: absolute;
    left: 140px;
    top: 170px;
    display: flex;
    align-items: center;
    gap: 26px;
  }
  .brand-dot { width: 110px; height: 110px; border-radius: 50%; background: var(--teal); }
  .brand-name { font-weight: 800; font-size: 40px; color: var(--ink); letter-spacing: 0.5px; }
</style>
</head>
<body>

<section class="card card-back">
  <svg class="card-art" viewBox="0 0 916 533" aria-hidden="true">
    <path fill="#ffffff" d="M426 172 C640 152 800 92 839 0 L884 0 C832 115 660 195 426 172 Z"/>
    <g fill="#ffffff">
      <path d="M335 68 l3 11 11 3 -11 3 -3 11 -3 -11 -11 -3 11 -3 Z"/>
      <path d="M574 56 l3 11 11 3 -11 3 -3 11 -3 -11 -11 -3 11 -3 Z"/>
      <path d="M410 306 l3 11 11 3 -11 3 -3 11 -3 -11 -11 -3 11 -3 Z"/>
      <path d="M778 472 l3 11 11 3 -11 3 -3 11 -3 -11 -11 -3 11 -3 Z"/>
    </g>
  </svg>

  <div class="back-brand">Hearthshine Crew</div>

  <div class="holder">
    <p class="holder-name">Corin ter Haghe</p>
    <p class="holder-role">Owner</p>
  </div>

  <ul class="contacts">
    <li class="contact">1300 482 916
      <svg viewBox="0 0 16 16" aria-hidden="true"><path fill="#fff" d="M3 1.5 l3 0 1 3.5 -2 1.3 c1 2 2.4 3.4 4.4 4.4 L10.7 8.7 14.5 9.7 14.5 12.8 C14.5 14 13.5 14.6 12.5 14.5 6.5 14 2 9.5 1.5 3.5 1.4 2.5 2 1.5 3 1.5 Z"/></svg>
    </li>
    <li class="contact">info@hearthshinecrew.com.au
      <svg viewBox="0 0 16 16" aria-hidden="true"><rect x="1" y="3" width="14" height="10" fill="#fff"/><path d="M1.5 3.5 L8 9 14.5 3.5" fill="none" stroke="#52c3cb" stroke-width="1.3"/></svg>
    </li>
    <li class="contact">www.hearthshinecrew.com.au
      <svg viewBox="0 0 16 16" aria-hidden="true"><circle cx="8" cy="8" r="7" fill="#fff"/><path d="M8 1 C5 4 5 12 8 15 M8 1 C11 4 11 12 8 15 M1 8 H15" fill="none" stroke="#52c3cb" stroke-width="1"/></svg>
    </li>
  </ul>
</section>

<section class="card card-front">
  <svg class="card-art" viewBox="0 0 916 533" aria-hidden="true">
    <path fill="#0d0d0d" d="M292 450 C520 432 720 360 788 210 C790 330 640 410 470 440 C410 450 350 453 292 450 Z"/>
    <path fill="#52c3cb" d="M289 469 C560 430 790 330 770 104 C880 175 890 330 640 420 C530 458 410 472 289 469 Z"/>
  </svg>

  <div class="front-brand">
    <span class="brand-dot"></span>
    <span class="brand-name">Hearthshine Crew</span>
  </div>
</section>

</body>
</html>
```